Full service meeting planning company needs new business cards

Bright Harbor is a full service meeting planning company that specializes in on-line conference registration web development and event communications. We combine citywide hotel management, mobile applications, eblast reminders, confirmation letters, and customized reporting to create a seamless registration process. We also manage group motor coach transportation, food and beverages, entertainment, stage and lighting for group of 10 to 4000.

Target Market(s)

Corporations and associations

Industry/Entity Type

Event Planning

Contact Information for Business Card

standard size 3.5" wide and 2" tall

Font styles to use
Serif
Sans Serif

Colors
f37122
f78f20
333333
5c5c5c
9d9d9d
f68d4d

Requirements
Must have
• {name}
• Bright Harbor
• P.O. Box 7384, Lakeview Falls, OR 97630
• www.brightharborplan.com
• {email}
• {phone}
• {mobile phone}
Nice to have
• Our colors are black, grey and orange as an accent color
Should not have
• I am not happy with our website layout anymore either. It feels dark and old but it does explain who we are pretty well if you'd like to review; www.brightharborplan.com

```html
<!DOCTYPE html>
<html lang="en">
<head>
<meta charset="utf-8">
<title>Bright Harbor — Business Card</title>
<link href="https://fonts.googleapis.com/css2?family=Montserrat:wght@400;700&family=Roboto:wght@300;400;700&display=swap" rel="stylesheet">
<style>
  :root {
    --page-bg: #e6e4e0;
    --card-dark: #2a2a2a;
    --card-dark-hi: #3a3a3a;
    --ink-white: #ffffff;
    --ink-soft: #d8d8d8;
    --rule: #6a6a6a;
    --band-grey: #9d9d9d;
    --tab-white: #f4f4f4;
    --tab-ink: #5c5c5c;
  }
  * { box-sizing: border-box; margin: 0; padding: 0; }
  html, body { width: 1200px; height: 950px; overflow: hidden; }
  body {
    background: var(--page-bg);
    font-family: "Roboto", Arial, sans-serif;
    position: relative;
  }
  .card {
    position: absolute;
    left: 250px;
    width: 700px;
    height: 400px;
    background: linear-gradient(135deg, var(--card-dark-hi) 0%, var(--card-dark) 55%, #222 100%);
    overflow: hidden;
    box-shadow: 0 10px 28px rgba(0,0,0,.28);
  }
  .card--front { top: 50px; }
  .card--back { top: 500px; }

  .brand {
    position: absolute;
    display: flex;
    flex-direction: column;
    align-items: center;
    gap: 16px;
  }
  .brand__mark {
    width: 96px; height: 96px;
    border-radius: 50%;
    background: var(--ink-white);
  }
  .brand__name {
    font-family: "Montserrat", Arial, sans-serif;
    font-weight: 700;
    color: var(--ink-white);
    font-size: 22px;
    letter-spacing: .5px;
    text-transform: uppercase;
    white-space: nowrap;
  }
  .card--front .brand { left: 0; right: 0; top: 125px; }

  .card--back .brand { left: 50px; top: 130px; width: 250px; }
  .card--back .brand__mark { width: 84px; height: 84px; }
  .card--back .brand__name { font-size: 19px; }

  .divider { position: absolute; left: 0; top: 0; }

  .contact {
    position: absolute;
    left: 385px;
    top: 50px;
    color: var(--ink-soft);
    font-size: 14px;
    line-height: 1.5;
    white-space: nowrap;
  }
  .contact__name {
    font-family: "Montserrat", Arial, sans-serif;
    font-weight: 700;
    color: var(--ink-white);
    font-size: 19px;
    text-transform: uppercase;
    line-height: 1.2;
  }
  .contact__title {
    font-size: 13px;
    text-transform: uppercase;
    letter-spacing: .5px;
    margin-bottom: 10px;
  }
  .contact__company { font-weight: 700; color: var(--ink-white); }
  .contact__lines { list-style: none; margin-top: 10px; }
  .contact__lines li { display: flex; align-items: center; gap: 10px; }
  .contact__lines svg { width: 14px; height: 14px; fill: var(--ink-white); flex: none; }

  .footer-art { position: absolute; left: 0; bottom: 0; }
  .web-tab {
    position: absolute;
    right: 22px;
    bottom: 30px;
    font-size: 15px;
    letter-spacing: 2.5px;
    color: var(--tab-ink);
  }
</style>
</head>
<body>

  <section class="card card--front" aria-label="Card front">
    <div class="brand">
      <div class="brand__mark"></div>
      <div class="brand__name">Bright Harbor</div>
    </div>
  </section>

  <section class="card card--back" aria-label="Card back">
    <svg class="divider" width="700" height="400" aria-hidden="true">
      <line x1="335" y1="45" x2="375" y2="270" stroke="var(--rule)" stroke-width="1.2"/>
    </svg>

    <div class="brand">
      <div class="brand__mark"></div>
      <div class="brand__name">Bright Harbor</div>
    </div>

    <div class="contact">
      <div class="contact__name">Mara Quillen</div>
      <div class="contact__title">President</div>
      <div class="contact__company">Bright Harbor</div>
      <div>P.O. Box 7384</div>
      <div>Lakeview Falls, OR 97630</div>
      <ul class="contact__lines">
        <li><svg viewBox="0 0 16 16"><path d="M3 2h3l1 4-2 1a9 9 0 0 0 4 4l1-2 4 1v3a2 2 0 0 1-2 2A12 12 0 0 1 1 4a2 2 0 0 1 2-2z"/></svg>214 7790 3061</li>
        <li><svg viewBox="0 0 16 16"><path d="M4 1h8a1 1 0 0 1 1 1v12a1 1 0 0 1-1 1H4a1 1 0 0 1-1-1V2a1 1 0 0 1 1-1zm1 2v9h6V3zm3 10a.8.8 0 1 0 0 1.6.8.8 0 0 0 0-1.6z"/></svg>415 2264 8817</li>
        <li><svg viewBox="0 0 16 16"><path d="M1 3h14v10H1zm1.5 1.2v.3L8 8.5l5.5-4v-.3zM2.5 6v5.8h11V6L8 10z"/></svg>mara@brightharborplan.com</li>
      </ul>
    </div>

    <svg class="footer-art" width="700" height="110" aria-hidden="true">
      <path d="M0 92 H700 V110 H0 Z" fill="var(--band-grey)"/>
      <path d="M390 92 V40 a22 22 0 0 1 22 -22 H700 V92 Z" fill="var(--tab-white)"/>
    </svg>
    <div class="web-tab">www.brightharborplan.com</div>
  </section>

</body>
</html>
```